Ecommerce Software Provider Needs A Fresh Look For Website

We are looking for a fresh, new look for our existing ecommerce software service. We provide an ecommerce software targeted at small business owners called "QuickelShop" and our existing website can be seen at http://www.quickelshop-example.com.

QuickelShop helps small business owners build their online store instantly without any coding. We focus on not just building "online stores" but PROFITABLE online stores. As such, we focus on tools and features that help our clients create online stores that convert.

The "feel" we want to portray to our clients are as below:

- Powerful
- Easy to use
- Can start quickly
- Successful
- Profitable

We are open to pretty much any color scheme or feel. The only thing we absolutely want to retain is our company logo which uses a shade of green and black.

So, this is pretty much a "free reign" kind of project. Let your imagination and design juices run wild! :-)

Industry/Entity Type

Small Business

```html
<!DOCTYPE html>
<html lang="en">
<head>
<meta charset="utf-8">
<title>QuickelShop – Ecommerce for Small Business</title>
<link rel="stylesheet" href="https://fonts.googleapis.com/css2?family=Yanone+Kaffeesatz:wght@300;400;600&family=Noto+Sans:wght@400&display=swap">
<style>
:root{
  --lime:#a4c31a;
  --lime-dark:#8fae10;
  --heading-green:#7da12a;
  --plum:#45313e;
  --panel:#e2e0e1;
  --ink:#2d2a2b;
  --white:#ffffff;
  --pink:#ee8b93;
}
*{box-sizing:border-box;margin:0;padding:0}
html,body{width:1200px;height:1000px;overflow:hidden;background:var(--white)}
body{position:relative;font-family:"Noto Sans",Verdana,sans-serif;color:var(--ink)}
.display{font-family:"Yanone Kaffeesatz",sans-serif;text-transform:uppercase}
.abs{position:absolute}

.top-bar{left:0;top:0;width:1200px;height:26px;background:var(--lime)}
.top-links{position:absolute;right:139px;top:5px;display:flex;gap:30px;font-family:"Yanone Kaffeesatz",sans-serif;font-size:15px;letter-spacing:.5px;color:var(--white)}

.brand{left:0;top:56px;width:1200px;display:flex;justify-content:center;align-items:center;gap:8px}
.brand-name{font-family:"Noto Sans",sans-serif;font-size:24px;font-weight:400;color:var(--ink)}
.brand-dot{width:22px;height:22px;border-radius:50%;background:var(--lime)}

.main-nav{left:138px;top:125px;width:924px;height:51px;background:var(--plum);display:flex;align-items:center;justify-content:space-between;padding:0 24px}
.main-nav a{font-family:"Yanone Kaffeesatz",sans-serif;font-size:16px;letter-spacing:.6px;color:#e8e2e6;text-decoration:none}
.main-nav a.current{color:var(--lime)}

.hero{left:138px;top:187px;width:612px;height:299px;background:linear-gradient(180deg,#ef9aa2 0 62px,#f6efe4 62px)}
.hero-art{position:absolute;left:86px;top:95px;width:432px;height:190px;background:linear-gradient(90deg,#f4c3cc,#f1a9b4 55%,#f6d6d6)}
.hero-band{position:absolute;left:0;top:138px;width:612px;height:86px;background:rgba(255,255,255,.72);display:flex;align-items:center;justify-content:center;text-align:center}
.hero-band p{font-family:"Yanone Kaffeesatz",sans-serif;font-size:26px;line-height:30px;color:#8ab53a;letter-spacing:.3px}
.dots{position:absolute;display:flex;gap:4px}
.dots span{width:14px;height:14px;border-radius:50%;background:#e6e6e6;border:1px solid #c9c9c9}
.dots span.on{background:var(--lime);border-color:var(--lime-dark)}
.dots.small span{width:9px;height:9px}

.latest{left:762px;top:187px;width:300px;height:299px;background:var(--panel)}
.panel-title{font-family:"Yanone Kaffeesatz",sans-serif;text-transform:uppercase;font-size:23px;color:var(--heading-green);letter-spacing:.3px}
.latest .panel-title{position:absolute;top:8px;width:100%;text-align:center}
.latest-shot{position:absolute;left:36px;top:40px;width:230px;height:230px;background:linear-gradient(180deg,#2b2b2b 0 22px,#f4f4f4 22px);box-shadow:0 3px 8px rgba(0,0,0,.35)}

.feature{top:497px;width:300px;height:221px;background:var(--panel)}
.feature .panel-title{position:absolute;left:24px;top:16px}
.feature-img{position:absolute;left:24px;top:49px;width:251px;height:74px}
.feature p{position:absolute;left:24px;top:134px;width:256px;font-size:12px;line-height:16.5px}
.btn-more{position:absolute;right:29px;top:190px;width:50px;height:17px;border-radius:4px;background:linear-gradient(#c2dc4a,#97b71a);color:var(--white);font-size:8px;line-height:17px;text-align:center;box-shadow:0 1px 2px rgba(0,0,0,.3)}

.what-we-do{left:138px;top:729px;width:924px;height:235px;background:radial-gradient(circle at 560px 40px,#b6d13a,var(--lime) 60%)}
.what-we-do h2{position:absolute;left:25px;top:20px;font-family:"Yanone Kaffeesatz",sans-serif;font-weight:400;font-size:35px;color:var(--white)}
.what-we-do p{position:absolute;left:25px;top:76px;width:425px;font-size:12px;line-height:18px;color:#eef5cf}
.btn-dark{position:absolute;left:362px;top:177px;width:84px;height:27px;border-radius:4px;background:#4d2f30;border:1px solid #d9d0c0;color:var(--white);font-size:12px;line-height:25px;text-align:center;box-shadow:0 2px 3px rgba(0,0,0,.35)}
.fan{position:absolute;left:470px;top:0;width:454px;height:235px;overflow:hidden}
.fan div{position:absolute;width:420px;height:300px;transform:rotate(16deg);transform-origin:0 0}

.section-title{top:972px;font-family:"Yanone Kaffeesatz",sans-serif;font-size:34px;font-weight:400;color:#3b2e32;letter-spacing:.5px}
.divider{left:525px;top:980px;width:1px;height:20px;background:#d0d0d0}
</style>
</head>
<body>
<div class="abs top-bar">
  <nav class="top-links"><span>MERCHANT LOGIN</span><span>SIGNUP NOW</span><span>FREE TRIAL</span></nav>
</div>

<div class="abs brand"><span class="brand-name">QuickelShop</span><span class="brand-dot"></span></div>

<nav class="abs main-nav">
  <a class="current">HOME</a><a>CART FEATURES</a><a>PRICING</a><a>CREDIT CARDS</a><a>HAPPY CLIENTS!</a><a>ECOMMERCE TEMPLATES</a><a>LIVE CHAT</a><a>E-BLOG</a><a>CONTACT</a>
</nav>

<section class="abs hero">
  <div class="hero-art" role="img" aria-label="Bakery store template preview with cupcakes and pink roses"></div>
  <div class="hero-band"><p>THE EASIEST POSSIBLE WAY TO GET A VISITOR'S<br>ATTENTION AND IMPROVE CONVERSION.</p></div>
  <div class="dots" style="left:538px;top:278px"><span class="on"></span><span></span><span></span><span></span></div>
</section>

<aside class="abs latest">
  <h3 class="panel-title">Latest Templates</h3>
  <div class="latest-shot" role="img" aria-label="Computer store template preview with laptops, tablets and monitors"></div>
  <div class="dots small" style="left:135px;top:279px"><span class="on"></span><span></span><span></span><span></span></div>
</aside>

<article class="abs feature" style="left:138px">
  <h3 class="panel-title">Beautiful Templates</h3>
  <div class="feature-img" role="img" aria-label="Template header with a martial arts belt photo" style="background:linear-gradient(90deg,#4b7a2e,#e9eef2 35%,#233f9a 70%,#e8e8ee)"></div>
  <p>Lorem ipsum dolor sit amet, consectetur adipiscing elit. Nunc porttitor, lacus et aliquam vehicula, nibh nisi varius mire.</p>
  <span class="btn-more">Read more</span>
</article>

<article class="abs feature" style="left:450px">
  <h3 class="panel-title">Accept Payments Easily</h3>
  <div class="feature-img" role="img" aria-label="Stack of colourful payment cards" style="background:linear-gradient(100deg,#3a64b0,#c9a457 40%,#d8624a 65%,#5a9a6a)"></div>
  <p>Lorem ipsum dolor sit amet, consectetur adipiscing elit. Nunc porttitor, lacus et aliquam vehicula, nibh nisi varius mire.</p>
  <span class="btn-more">Read more</span>
</article>

<article class="abs feature" style="left:762px">
  <h3 class="panel-title">Sell on Friendspace</h3>
  <div class="feature-img" role="img" aria-label="Shopping cart on a blue social network banner" style="background:linear-gradient(90deg,#4a6fb0,#3b5998)"></div>
  <p>Lorem ipsum dolor sit amet, consectetur adipiscing elit. Nunc porttitor, lacus et aliquam vehicula, nibh nisi varius mire.</p>
  <span class="btn-more">Read more</span>
</article>

<section class="abs what-we-do">
  <h2>WHAT WE DO.....</h2>
  <p>Lorem ipsum dolor sit amet, consectetur adipiscing elit. Nunc porttitor, lacus et aliquam vehicula, nibh nisi varius mi, in varius tellus enim in leo. Vivamus nec ante neque. Quisque ullamcorper augue et sagittis dignissim. Phasellus consequat ipsum leo, ac viverra urna dictum nec. Morbi vitae tempus magna.</p>
  <span class="btn-dark">Read more</span>
  <div class="fan" role="img" aria-label="Fanned stack of store template previews">
    <div style="left:150px;top:-10px;background:#1f7a78"></div>
    <div style="left:230px;top:15px;background:#f0b49a"></div>
    <div style="left:80px;top:25px;background:linear-gradient(180deg,#ee8b93 0 40px,#f8f1e8 40px)"></div>
  </div>
</section>

<h2 class="abs section-title" style="left:138px">WHY US</h2>
<div class="abs divider"></div>
<h2 class="abs section-title" style="left:545px">TESTIMONIALS</h2>
</body>
</html>
```